ridge-mosaic builders & interiors

I need a web design for my company we offer counter tops. tile for floors,showers,kitchen backsplashes and more also need a place where the client
can write reviews

Industry/Entity Type

Tile

```html
<!DOCTYPE html>
<html lang="en">
<head>
<meta charset="utf-8">
<title>Ridge-Mosaic Builders &amp; Interiors</title>
<link rel="stylesheet" href="https://fonts.googleapis.com/css2?family=Libre+Baskerville&family=Open+Sans:wght@400;600;700&family=Oswald:wght@300&display=swap">
<style>
:root{
  --header:#4d321f;
  --top-strip:#604731;
  --body:#5b3f29;
  --panel:#6b5039;
  --banner:#0a0807;
  --cream:#e9dcc8;
  --tan:#c7ab86;
  --muted:#b9a58c;
  --light-bg:#eeeef2;
  --ink-dark:#4a2f1c;
  --line-light:#9a8f86;
  --footer:#4f3420;
  --footer-bar:#654a33;
  --footer-text:#b39c80;
}
*{margin:0;padding:0;box-sizing:border-box}
html,body{width:718px;height:1200px;overflow:hidden}
body{position:relative;background:var(--body);font-family:"Open Sans",sans-serif;color:var(--cream)}
.abs{position:absolute}
.site-header{left:0;top:0;width:718px;height:98px;background:var(--header);border-top:10px solid var(--top-strip)}
.brand{left:203px;top:22px;width:336px;height:35px;border-top:1px solid var(--tan);border-bottom:1px solid var(--tan);display:flex;align-items:center;justify-content:center;font-family:"Libre Baskerville",serif;font-size:15.5px;color:var(--cream);text-transform:uppercase;letter-spacing:.2px;white-space:nowrap}
.main-nav{left:0;top:68px;width:718px;display:flex;justify-content:center;gap:14px;font-family:"Libre Baskerville",serif;font-size:8.5px;color:var(--cream);letter-spacing:.4px}
.main-nav span.dot{color:var(--tan)}
.hero{left:0;top:98px;width:718px;height:361px;background:linear-gradient(100deg,#6a4a30 0%,#d9d3c8 30%,#efece6 50%,#7a5536 70%,#3f2c1e 100%)}
.offer-panel{left:16px;top:417px;width:689px;height:337px;background:var(--panel)}
.offer-banner{left:24px;top:424px;width:674px;height:78px;background:var(--banner);text-align:center}
.offer-title{margin-top:16px;font-family:"Libre Baskerville",serif;font-size:15px;color:var(--cream);letter-spacing:.6px}
.offer-rule{width:286px;height:1px;background:#6a5644;margin:5px auto 6px}
.offer-note{font-size:9.5px;color:var(--tan)}
.section-title{font-family:"Libre Baskerville",serif;text-transform:uppercase}
.featured-title{left:32px;top:525px;font-size:13px;color:var(--cream)}
.featured-rule{left:32px;top:545px;width:644px;height:1px;background:#86705a}
.carousel-arrows{left:645px;top:525px}
.product{width:137px}
.product-photo{width:137px;height:130px;border:2px solid #e6ddd0}
.product-name{margin-top:12px;font-size:8.5px;font-weight:700;color:var(--cream)}
.product-desc{margin-top:1px;font-family:"Libre Baskerville",serif;font-size:8.5px;color:var(--muted)}
.product-price{margin-top:2px;font-family:"Oswald",sans-serif;font-weight:300;font-size:18px;color:var(--muted);letter-spacing:-.6px}
.testimonials{left:0;top:766px;width:718px;height:199px;background:var(--light-bg)}
.testimonials-title{left:25px;top:780px;font-size:15.5px;color:var(--ink-dark)}
.testimonials-rule{left:22px;top:802px;width:668px;height:1px;background:var(--line-light)}
.review{width:200px;height:125px}
.avatar{position:absolute;left:0;top:0;width:36px;height:46px;border:1px solid #8b8580;background:linear-gradient(160deg,#b8a392,#5b4a40)}
.bubble{position:absolute;left:51px;top:0;width:141px;height:90px;border:1px solid var(--ink-dark);background:#fff;padding:7px 6px 0 8px;font-family:Arial,sans-serif;font-size:8.3px;line-height:1.27;color:#333}
.bubble::before{content:"";position:absolute;left:-8px;top:13px;border:4px solid transparent;border-right:5px solid var(--ink-dark)}
.reviewer{position:absolute;left:50px;top:99px;font-family:Arial,sans-serif;font-size:10px;font-weight:700;color:#7a5a40}
.reviewer-role{position:absolute;left:50px;top:111px;font-family:Arial,sans-serif;font-size:8.5px;color:#999}
.site-footer{left:0;top:965px;width:718px;height:182px;background:var(--footer)}
.footer-col{top:990px}
.footer-heading{font-size:15px;color:var(--footer-text);padding-bottom:4px;border-bottom:1px solid #7d6650}
.footer-about{margin-top:18px;font-size:8.4px;line-height:1.3;color:var(--footer-text)}
.footer-links{margin-top:20px;display:grid;grid-template-columns:125px 100px;row-gap:11px;font-size:7.8px;font-weight:700;color:var(--footer-text);padding-left:2px}
.social{margin-top:20px;display:flex;gap:8px}
.social span{width:22px;height:22px;border-radius:50%;background:#9a8672}
.contact-info{margin-top:10px;font-family:Arial,sans-serif;font-size:8.5px;line-height:1.3;color:#a8937a}
.footer-bar{left:0;top:1147px;width:718px;height:41px;background:var(--footer-bar)}
.copyright{left:15px;top:1163px;font-size:7.8px;color:#d2c2ad}
.footer-brand{left:499px;top:1155px;padding-bottom:4px;border-top:1px solid #8b7258;border-bottom:1px solid #8b7258;font-family:"Libre Baskerville",serif;font-size:9.5px;color:var(--footer-text);text-transform:uppercase;padding-top:3px}
.base-strip{left:0;top:1188px;width:718px;height:12px;background:var(--header)}
</style>
</head>
<body>
<header class="site-header abs"></header>
<div class="brand abs">Ridge-Mosaic Builders &amp; Interiors</div>
<nav class="main-nav abs">
  <span>HOME</span><span class="dot">·</span><span>ABOUT US</span><span class="dot">·</span><span>PRODUCTS</span><span class="dot">·</span><span>CONTACT US</span>
</nav>

<div class="hero abs" role="img" aria-label="Photo of a wood-panelled kitchen with a white-topped island"></div>

<section class="offer-panel abs"></section>
<div class="offer-banner abs">
  <p class="offer-title">FREE SHIPPING ON ALL ORDERS OVER $150</p>
  <div class="offer-rule"></div>
  <p class="offer-note">NO REQUIREMENTS REQUIRED JUST SHOP ABOVE $150</p>
</div>

<h2 class="section-title featured-title abs">Featured Products</h2>
<div class="featured-rule abs"></div>
<svg class="carousel-arrows abs" width="30" height="14" viewBox="0 0 30 14" aria-label="Previous and next">
  <path d="M11 1 L1 7 L11 13 Z" fill="#e6ddd0"/><path d="M18 1 L28 7 L18 13 Z" fill="#e6ddd0"/>
</svg>

<div class="product abs" style="left:33px;top:555px">
  <div class="product-photo" role="img" aria-label="Photo of a granite kitchen island" style="background:linear-gradient(170deg,#6e4b30,#c9ad84 55%,#8a6a4a)"></div>
  <p class="product-name">PRODUCT NAME</p><p class="product-desc">Honed Granite Counter Slab</p><p class="product-price">$101.23</p>
</div>
<div class="product abs" style="left:202px;top:555px">
  <div class="product-photo" role="img" aria-label="Photo of a gold-veined stone countertop" style="background:linear-gradient(170deg,#5a3b24,#b58650 55%,#d7b27c)"></div>
  <p class="product-name">PRODUCT NAME</p><p class="product-desc">Honed Granite Counter Slab</p><p class="product-price">$101.23</p>
</div>
<div class="product abs" style="left:370px;top:555px">
  <div class="product-photo" role="img" aria-label="Photo of a curved dark granite countertop" style="background:linear-gradient(170deg,#a98a6e,#3d4448 50%,#6a4a34)"></div>
  <p class="product-name">PRODUCT NAME</p><p class="product-desc">Honed Granite Counter Slab</p><p class="product-price">$101.23</p>
</div>
<div class="product abs" style="left:539px;top:555px">
  <div class="product-photo" role="img" aria-label="Photo of a white quartz counter with brick backsplash" style="background:linear-gradient(170deg,#8a4a36,#e8e6e2 50%,#6a3a26)"></div>
  <p class="product-name">PRODUCT NAME</p><p class="product-desc">Honed Granite Counter Slab</p><p class="product-price">$101.23</p>
</div>

<section class="testimonials abs"></section>
<h2 class="section-title testimonials-title abs">Testimonials</h2>
<div class="testimonials-rule abs"></div>

<div class="review abs" style="left:21px;top:826px">
  <div class="avatar" role="img" aria-label="Portrait of the reviewer"></div>
  <p class="bubble">Ut enim ad minim veniam, quis nostrud exercitation ullamco laboris nisi ut aliquip ex ea commodo consequat. Duis aute irure dolor in reprehenderit in voluptate velit esse cillum dolore eu fugiat nulla pariatur.</p>
  <p class="reviewer">Ravi Castellan</p><p class="reviewer-role">Real Estate Guru</p>
</div>
<div class="review abs" style="left:260px;top:826px">
  <div class="avatar" role="img" aria-label="Portrait of the reviewer"></div>
  <p class="bubble">Ut enim ad minim veniam, quis nostrud exercitation ullamco laboris nisi ut aliquip ex ea commodo consequat. Duis aute irure dolor in reprehenderit in voluptate velit esse cillum dolore eu fugiat nulla pariatur.</p>
  <p class="reviewer">Nora Whitfield</p><p class="reviewer-role">Interior Designer</p>
</div>
<div class="review abs" style="left:500px;top:826px">
  <div class="avatar" role="img" aria-label="Portrait of the reviewer"></div>
  <p class="bubble">Ut enim ad minim veniam, quis nostrud exercitation ullamco laboris nisi ut aliquip ex ea commodo consequat. Duis aute irure dolor in reprehenderit in voluptate velit esse cillum dolore eu fugiat nulla pariatur.</p>
  <p class="reviewer">Owen Tarrant</p><p class="reviewer-role">Civil Engineer</p>
</div>

<footer class="site-footer abs"></footer>
<div class="footer-col abs" style="left:12px;width:208px">
  <h3 class="section-title footer-heading">About Us</h3>
  <p class="footer-about">Lorem ipsum dolor sit amet, consectetur adipisicing elit, sed do eiusmod tempor incididunt ut labore et dolore magna aliqua. Ut enim ad minim veniam, quis nostrud exercitation ullamco laboris nisi ut aliquip ex ea commodo consequat.</p>
</div>
<div class="footer-col abs" style="left:258px;width:208px">
  <h3 class="section-title footer-heading">Information</h3>
  <div class="footer-links">
    <span>TRACK ORDERS</span><span>BLOG</span>
    <span>FAQS</span><span>ABOUT US</span>
    <span>PORTFOLIO</span><span>SERVICES</span>
    <span>SHOP SALES</span><span>CONTACT US</span>
  </div>
</div>
<div class="footer-col abs" style="left:498px;width:208px">
  <h3 class="section-title footer-heading">Connect</h3>
  <div class="social"><span></span><span></span><span></span><span></span><span></span></div>
  <p class="contact-info">412 Quarry Lane<br>Brookvale, BV7 2KL.<br>Phone: +1 555 014 2290</p>
</div>

<div class="footer-bar abs"></div>
<p class="copyright abs">© Copyright Ridge-Mosaic 2014. All Rights Reserved</p>
<p class="footer-brand abs">Ridge-Mosaic Builders &amp; Interiors</p>
<div class="base-strip abs"></div>
</body>
</html>
```